Flyer-Design für Vertrieb von Verpackungsmaterial
Zielgruppe
Vertrieb von Verpackungsmaterial. Zielgruppe: primär Bäckreien, Konditoreien, usw.
Aufgabenstellung
De Flyer wird als Inlet für einen Muserbeutel für Verschlussklammern und Fertigschlafen verwendet. Grösse Din A6, vor und Rückseite.
Vorderseite: U-Clipse und Streifenverschlüsse
Rückseite: Fertigschlaufen

```html
<!DOCTYPE html>
<html lang="de">
<head>
<meta charset="utf-8">
<title>Verschlussklammern und Fertigschleifen – Flyer</title>
<link href="https://fonts.googleapis.com/css2?family=Fira+Sans:wght@300;400;600;700;800&display=swap" rel="stylesheet">
<style>
:root{
  --wine:#6f2428;
  --title:#7a2229;
  --band:#8c4a4c;
  --frame:#a0605f;
  --ink:#3a3434;
  --stage:#e9e4e3;
  --black:#1c1c1c;
  --table-bg:#fafafa;
}
*{box-sizing:border-box;margin:0;padding:0}
html,body{width:1200px;height:800px;overflow:hidden}
body{background:var(--stage);font-family:"Fira Sans",sans-serif;position:relative;color:var(--ink)}
.flyer{position:absolute;top:101px;width:424px;height:598px;background:linear-gradient(160deg,#f7f7f7,#e9e9e9);box-shadow:0 4px 14px rgba(0,0,0,.15);overflow:hidden}
.flyer--front{left:138px}
.flyer--back{left:636px}
.frame{position:absolute;left:16px;top:17px;width:392px;height:511px;border-left:1px solid var(--frame);border-right:1px solid var(--frame)}
.frame::before,.frame::after{content:"";position:absolute;top:0;width:6px;border-top:1px solid var(--frame)}
.frame::before{left:0}.frame::after{right:0}
.headline{position:absolute;left:0;right:0;top:15px;text-align:center;color:var(--title)}
.headline h1{font-weight:700;letter-spacing:2px;line-height:1}
.headline p{font-weight:400;font-size:16px;margin-top:4px}
.flyer--front .headline h1{font-size:26px}
.flyer--back .headline h1{font-size:33px;letter-spacing:3px}
.flyer--back .headline p{margin-top:3px}

.spec{position:absolute;background:var(--band)}
.spec__label{position:absolute;left:0;top:0;bottom:0;width:32px;display:flex;align-items:center;justify-content:center;color:#fff}
.spec__label span{writing-mode:vertical-rl;transform:rotate(180deg);font-weight:700;font-size:12px;white-space:nowrap;line-height:1.15}
.spec__label b{font-weight:700;font-size:11px}
.spec__label small{font-weight:300;font-size:8px}
.spec__label .sub{display:block;font-weight:300;font-size:8px}
.spec__head{position:absolute;left:32px;top:0;height:16px;display:flex;color:#fff;font-size:7.5px;font-weight:600;align-items:center}
.spec__head span{padding-left:7px;white-space:nowrap}
.spec__table{position:absolute;left:32px;top:16px;bottom:2px;table-layout:fixed;border-collapse:collapse;background:var(--table-bg);font-size:10px;font-weight:300;color:var(--ink)}
.spec__table td{border-left:1px solid var(--band);padding:0 0 0 7px;line-height:12.6px;vertical-align:top;white-space:nowrap;overflow:hidden}
.spec__table td:first-child{border-left:none}
.spec__table .gap td{height:6px}
.spec__table .pad td{height:10px}

.spec--clips{left:31px;top:102px;width:224px;height:168px}
.spec--clips .spec__table,.spec--clips .spec__head{width:190px}
.spec--strips{left:206px;top:288px;width:193px;height:240px}
.spec--strips .spec__table,.spec--strips .spec__head{width:159px}
.spec--strips .gap td{height:6.5px}
.spec--bows{left:31px;top:102px;width:214px;height:161px}
.spec--bows .spec__table,.spec--bows .spec__head{width:180px}

.photo{position:absolute;border-radius:50%;border:2px solid #fff;box-shadow:0 2px 6px rgba(0,0,0,.35)}
.photo--clip{left:225px;top:72px;width:104px;height:104px;background:radial-gradient(circle at 45% 50%,#b39a4c 0 28%,#141414 55%)}
.photo--strip{left:72px;top:334px;width:96px;height:96px;background:linear-gradient(160deg,#141414 30%,#d8d3c6 38%,#b39a4c 48%,#141414 58%)}
.photo--red{left:221px;top:80px;width:100px;height:100px;background:radial-gradient(circle,#9a1b20 0 40%,#efefef 62%)}
.photo--gold{left:283px;top:154px;width:88px;height:88px;background:radial-gradient(circle,#b88a45 0 40%,#efefef 62%)}
.strips{position:absolute;left:0;top:0;width:424px;height:598px}

.bows{position:absolute;left:8px;top:322px;width:410px;height:180px;display:grid;grid-template-columns:repeat(4,1fr);gap:12px}
.bow{border-radius:40% 40% 46% 46%}
.bow--rot{background:radial-gradient(ellipse,#8e1a20 30%,transparent 70%)}
.bow--gelb{background:radial-gradient(ellipse,#d7b520 30%,transparent 70%)}
.bow--hellgruen{background:radial-gradient(ellipse,#6d9a3a 30%,transparent 70%)}
.bow--dunkelgruen{background:radial-gradient(ellipse,#16302e 30%,transparent 70%)}
.bow--blau{background:radial-gradient(ellipse,#2a2282 30%,transparent 70%)}
.bow--gold{background:radial-gradient(ellipse,#b4823f 30%,transparent 70%)}
.bow--creme{background:radial-gradient(ellipse,#dcd9c8 30%,transparent 70%)}
.bow--weiss{background:radial-gradient(ellipse,#d2d2dc 30%,transparent 70%)}

.footer{position:absolute;left:0;right:0;bottom:0;height:61px;background:var(--wine);color:#fff}
.footer__web{position:absolute;left:30px;top:9px;font-size:17px;font-weight:700}
.footer__contact{position:absolute;left:30px;top:36px;font-size:10px;font-weight:300}
.footer__brand{position:absolute;right:0;top:13px;width:165px;height:34px;background:var(--black);display:flex;align-items:center;justify-content:flex-end;padding-right:8px;font-size:15px;font-weight:700;color:#fff}
</style>
</head>
<body>

<section class="flyer flyer--front">
  <div class="frame"></div>
  <header class="headline">
    <h1>VERSCHLUSSKLAMMERN</h1>
    <p>Auch in kleinen Mengen erhätlich.</p>
  </header>

  <div class="spec spec--clips">
    <div class="spec__label"><span>U-Clipse</span></div>
    <div class="spec__head"><span style="width:46px">Art.-Nr.</span><span style="width:58px">Länge/Breite</span><span>Farbe</span></div>
    <table class="spec__table">
      <colgroup><col style="width:46px"><col style="width:58px"><col style="width:86px"></colgroup>
      <tr class="pad"><td></td><td></td><td></td></tr>
      <tr><td>10'701</td><td>33/8 mm</td><td>gold</td></tr>
      <tr><td>10'702</td><td>33/8 mm</td><td>silber</td></tr>
      <tr><td>10'703</td><td>33/8 mm</td><td>weiss</td></tr>
      <tr><td>10'704</td><td>33/8 mm</td><td>blau / weiss</td></tr>
      <tr><td>10'705</td><td>33/8 mm</td><td>rot / weiss</td></tr>
      <tr class="gap"><td></td><td></td><td></td></tr>
      <tr><td>10'706</td><td>40/8 mm</td><td>gold</td></tr>
      <tr><td>10'707</td><td>40/8 mm</td><td>silber</td></tr>
      <tr><td>70'708</td><td>40/8 mm</td><td>weiss</td></tr>
      <tr><td>10'709</td><td>40/8 mm</td><td>blau / weiss</td></tr>
      <tr><td>10'710</td><td>40/8 mm</td><td>rot / weiss</td></tr>
      <tr><td></td><td></td><td></td></tr>
    </table>
  </div>
  <div class="photo photo--clip" role="img" aria-label="Nahaufnahme eines goldenen U-Clips"></div>

  <svg class="strips" viewBox="0 0 424 598" role="img" aria-label="Weisser und goldener Streifenverschluss">
    <line x1="74" y1="545" x2="214" y2="374" stroke="#dadada" stroke-width="6"/>
    <line x1="155" y1="545" x2="204" y2="343" stroke="#c9a56c" stroke-width="7"/>
  </svg>
  <div class="photo photo--strip" role="img" aria-label="Nahaufnahme weisser und goldener Streifenverschlüsse"></div>

  <div class="spec spec--strips">
    <div class="spec__label"><span>Streifenverschlüsse</span></div>
    <div class="spec__head"><span style="width:46px">Art.-Nr.</span><span style="width:62px">Länge/Breite</span><span>Farbe</span></div>
    <table class="spec__table">
      <colgroup><col style="width:46px"><col style="width:62px"><col style="width:51px"></colgroup>
      <tr class="pad"><td></td><td></td><td></td></tr>
      <tr><td>10'700</td><td>55/8 mm</td><td>weiss</td></tr>
      <tr class="gap"><td></td><td></td><td></td></tr>
      <tr><td>10'711</td><td>80/8 mm</td><td>gold</td></tr>
      <tr><td>10'712</td><td>80/8 mm</td><td>weiss</td></tr>
      <tr class="gap"><td></td><td></td><td></td></tr>
      <tr><td>10'714</td><td>100/8 mm</td><td>gold</td></tr>
      <tr><td>10'715</td><td>100/8 mm</td><td>weiss</td></tr>
      <tr class="gap"><td></td><td></td><td></td></tr>
      <tr><td>10'717</td><td>120/8 mm</td><td>gold</td></tr>
      <tr><td>10'718</td><td>120/8 mm</td><td>weiss</td></tr>
      <tr class="gap"><td></td><td></td><td></td></tr>
      <tr><td>10'720</td><td>140/8 mm</td><td>gold</td></tr>
      <tr><td>10'721</td><td>140/8 mm</td><td>weiss</td></tr>
      <tr class="gap"><td></td><td></td><td></td></tr>
      <tr><td>10'723</td><td>160/8 mm</td><td>gold</td></tr>
      <tr><td>10'724</td><td>160/8 mm</td><td>weiss</td></tr>
      <tr class="gap"><td></td><td></td><td></td></tr>
      <tr><td>10'726</td><td>180/8 mm</td><td>gold</td></tr>
      <tr><td>10'727</td><td>180/8 mm</td><td>weiss</td></tr>
      <tr><td></td><td></td><td></td></tr>
    </table>
  </div>

  <footer class="footer">
    <div class="footer__web">www.brenner-pack.ch</div>
    <div class="footer__contact">Tel. 044 5550123 | info@brenner-pack.ch</div>
    <div class="footer__brand">brenner pack</div>
  </footer>
</section>

<section class="flyer flyer--back">
  <div class="frame"></div>
  <header class="headline">
    <h1>FERTIGSCHLEIFEN</h1>
    <p>Auch in kleinen Mengen erhätlich.</p>
  </header>

  <div class="spec spec--bows">
    <div class="spec__label"><span><b>Fertigschleifen</b> <small>auf 50 mm</small><span class="sub">Clipband Gold aus 10 mm Satinband</span></span></div>
    <div class="spec__head"><span style="width:46px">Art.-Nr.</span><span style="width:60px">Länge/Breite</span><span>Farbe</span></div>
    <table class="spec__table">
      <colgroup><col style="width:46px"><col style="width:60px"><col style="width:74px"></colgroup>
      <tr class="pad"><td style="height:16px"></td><td></td><td></td></tr>
      <tr><td>10'810</td><td>60x40/10</td><td>rot</td></tr>
      <tr><td>10'811</td><td>60x40/10</td><td>gelb</td></tr>
      <tr><td>10'812</td><td>60x40/10</td><td>hellgrün</td></tr>
      <tr><td>10'813</td><td>60x40/10</td><td>dunkelgrün</td></tr>
      <tr><td>10'814</td><td>60x40/10</td><td>blau</td></tr>
      <tr><td>10'815</td><td>60x40/10</td><td>gold</td></tr>
      <tr><td>10'816</td><td>60x40/10</td><td>crème</td></tr>
      <tr><td>10'817</td><td>60x40/10</td><td>weiss</td></tr>
      <tr><td></td><td></td><td></td></tr>
    </table>
  </div>
  <div class="photo photo--red" role="img" aria-label="Rote Satinschleife auf goldenem Clipband"></div>
  <div class="photo photo--gold" role="img" aria-label="Goldene Satinschleife auf goldenem Clipband"></div>

  <div class="bows">
    <div class="bow bow--rot" role="img" aria-label="Rote Fertigschleife"></div>
    <div class="bow bow--gelb" role="img" aria-label="Gelbe Fertigschleife"></div>
    <div class="bow bow--hellgruen" role="img" aria-label="Hellgrüne Fertigschleife"></div>
    <div class="bow bow--dunkelgruen" role="img" aria-label="Dunkelgrüne Fertigschleife"></div>
    <div class="bow bow--blau" role="img" aria-label="Blaue Fertigschleife"></div>
    <div class="bow bow--gold" role="img" aria-label="Goldene Fertigschleife"></div>
    <div class="bow bow--creme" role="img" aria-label="Crèmefarbene Fertigschleife"></div>
    <div class="bow bow--weiss" role="img" aria-label="Weisse Fertigschleife"></div>
  </div>

  <footer class="footer">
    <div class="footer__web">www.brenner-pack.ch</div>
    <div class="footer__contact">Tel. 044 5550123 | info@brenner-pack.ch</div>
    <div class="footer__brand">brenner pack</div>
  </footer>
</section>

</body>
</html>
```